PROFESSIONAL MODERN REDESIGN OF CURRENT WEBSITE USING ALL SAME CONTENT

I need to redesign existing website using all existing exact content. Please do not leave anything missing. Use all content.

www.brightpathpromotionsgroup.biz

Target Market(s)

Small business owners, business to business, B2B

Industry/Entity Type

Direct Marketing

Number of Pages Required

5+ page

Colors

Designer to choose colors to be used in the design.

Requirements
Must have
• Must use exact same content as www.brightpathpromotionsgroup.biz
Nice to have
• I'd like this to be an easy to read professionally designed website with all modern elements...
Should not have
• Open

```html
<!DOCTYPE html>
<html lang="en">
<head>
<meta charset="utf-8">
<title>BrightPath Promotions Group — Premium Incentive Marketing Services</title>
<link href="https://fonts.googleapis.com/css2?family=Dosis:wght@500;600;700&family=Raleway:wght@400;500;600&display=swap" rel="stylesheet">
<style>
:root{
  --blue:#1573c6;
  --blue-dark:#0f5da3;
  --orange:#f7931e;
  --orange-text:#f39220;
  --teal-dark:#0e3b44;
  --teal:#1a5560;
  --ink:#2b2b2b;
  --muted:#6c6c6c;
  --line:#d8d8d8;
  --pale:#f4f6f9;
  --white:#fff;
}
*{box-sizing:border-box;margin:0;padding:0}
html,body{width:1200px;height:3417px;overflow:hidden}
body{font-family:"Raleway",sans-serif;color:var(--ink);background:var(--white);position:relative}
.heading{font-family:"Dosis",sans-serif;font-weight:600;color:var(--orange-text);text-align:center;font-size:31px;letter-spacing:.2px}
.sub{font-size:12px;color:var(--muted);text-align:center;line-height:17px}
.btn{display:inline-block;background:var(--blue);color:#fff;font-family:"Dosis",sans-serif;font-weight:600;font-size:13px;border-radius:26px;height:50px;line-height:50px;padding:0 26px;box-shadow:0 6px 14px rgba(21,115,198,.35);text-decoration:none}
.center{text-align:center}

/* header */
.site-header{position:absolute;top:0;left:0;width:1200px;height:102px;background:#fff}
.brand{position:absolute;left:86px;top:30px;display:flex;align-items:center;gap:10px;font-family:"Dosis",sans-serif;font-weight:700;font-size:23px;color:var(--blue)}
.brand-dot{width:14px;height:14px;background:var(--blue);border-radius:50%}
.top-links{position:absolute;left:733px;top:17px;font-size:14px;color:#7aa4cf;display:flex;gap:32px}
.contact-line{position:absolute;left:893px;top:13px;display:flex;align-items:center;gap:12px}
.phone-badge{width:34px;height:34px;border-radius:50%;background:var(--blue);display:flex;align-items:center;justify-content:center}
.contact-line p{font-size:10px;line-height:14px;color:#333}
.header-rule{position:absolute;left:733px;top:52px;width:380px;height:1px;background:#bbb}
.main-nav{position:absolute;left:498px;top:68px;display:flex;gap:34px;font-size:14px;color:#333}
.main-nav .active{color:var(--blue)}

/* hero */
.hero{position:absolute;top:102px;left:0;width:1200px;height:472px;background:linear-gradient(100deg,#0b2f37 0%,#1a4f5a 45%,#0f3a44 75%,#0a2a33 100%);overflow:hidden}
.hero-copy{position:absolute;top:168px;width:100%;text-align:center}
.hero-copy h1{font-family:"Dosis",sans-serif;font-weight:700;font-size:36px;color:var(--orange)}
.hero-copy p{font-family:"Dosis",sans-serif;font-weight:600;font-size:17px;color:#fff;line-height:26px;margin-top:6px}
.hero-actions{position:absolute;top:305px;left:427px;display:flex;align-items:center;gap:26px}
.watch{display:flex;align-items:center;gap:10px;font-family:"Dosis",sans-serif;font-weight:600;font-size:13px;color:#fff}
.watch span{width:32px;height:32px;border:2px solid #fff;border-radius:50%;display:flex;align-items:center;justify-content:center}
.hero-shapes{position:absolute;top:0;left:0}

/* stats */
.right-fit{position:absolute;top:666px;width:1200px;height:310px}
.right-fit .heading{margin-top:3px}
.stats{position:absolute;top:115px;left:100px;width:1000px;display:flex;justify-content:space-between}
.stat{width:150px;text-align:center;font-family:"Dosis",sans-serif;font-weight:500;font-size:16px;color:#333;line-height:20px}
.stat svg{display:block;margin:0 auto 12px}

/* gift certificates */
.certs{position:absolute;top:975px;width:1200px;height:570px;background:linear-gradient(#fff,#f3f5f8)}
.certs .heading{margin-top:53px}
.certs .sub{width:460px;margin:10px auto 0;font-size:11px}
.cert-grid{position:absolute;top:192px;left:93px;display:flex;gap:17px}
.cert{width:240px;text-align:center}
.cert-photo{height:120px;border-top:3px solid var(--blue)}
.cert-label{background:var(--blue);color:#fff;font-family:"Dosis",sans-serif;font-weight:600;font-size:14px;height:52px;line-height:52px}
.cert-text{font-size:12px;color:#555;line-height:21px;margin-top:12px;height:66px}
.cert-text b{color:var(--blue);font-weight:600}
.cert-link{font-family:"Dosis",sans-serif;font-weight:600;font-size:13px;color:var(--blue);margin-top:10px;display:flex;justify-content:center;gap:18px;align-items:center}
.certs .btn{position:absolute;top:509px;left:497px;height:52px;line-height:52px;padding:0 14px}

/* advertising areas */
.areas{position:absolute;top:1545px;width:1200px;height:586px;background:linear-gradient(90deg,#dfe6ee,#f4f6f8 30%,#f4f6f8 70%,#d9e0e8)}
.areas .heading{margin-top:82px}
.area{position:absolute;width:335px;height:127px;background:#fff;display:flex;box-shadow:0 2px 8px rgba(0,0,0,.08)}
.area-photo{width:128px;flex:none}
.area-body{padding:8px 8px}
.area-body h3{font-family:"Dosis",sans-serif;font-weight:600;font-size:14px;line-height:18px;color:#222}
.area-body p{font-size:10px;line-height:17px;color:#777;margin-top:5px}
.areas .btn{position:absolute;top:515px;left:497px;height:52px;line-height:52px;padding:0 19px}

/* distribution */
.distribution{position:absolute;top:2131px;width:1200px;height:495px;background:var(--blue);color:#fff;overflow:hidden}
.distribution .heading{margin-top:40px;color:var(--orange)}
.channel{position:absolute;top:116px;width:260px;text-align:center}
.ring{width:100px;height:100px;margin:0 auto;border-radius:50%;background:#fff;border:6px solid var(--orange);display:flex;align-items:center;justify-content:center}
.channel h3{font-family:"Dosis",sans-serif;font-weight:600;font-size:19px;margin-top:18px}
.channel p{font-size:12px;line-height:19px;margin-top:14px}
.connector{position:absolute;top:150px}
.call-btn{position:absolute;top:419px;left:497px;width:206px;height:52px;line-height:52px;border-radius:26px;background:#fff;color:var(--blue);text-align:center;font-family:"Dosis",sans-serif;font-weight:600;font-size:13px}
.call-btn em{font-style:normal;color:var(--orange)}

/* promotional materials */
.materials{position:absolute;top:2626px;width:1200px;height:791px;background:linear-gradient(#f5f6f8,#fff 60%)}
.materials .heading{margin-top:68px;line-height:31px}
.mat-grid{position:absolute;top:176px;left:93px;display:flex;gap:17px}
.mat{width:240px}
.mat-photo{height:118px;border-top:3px solid var(--blue)}
.mat-label{background:var(--blue);color:#fff;font-family:"Dosis",sans-serif;font-weight:600;font-size:20px;text-align:center;height:52px;line-height:52px}
.offer-box{position:absolute;top:473px;left:227px;width:273px;height:291px;background:var(--blue);color:#fff;text-align:center;box-shadow:0 6px 14px rgba(0,0,0,.15)}
.offer-box h3{font-family:"Dosis",sans-serif;font-weight:600;font-size:18px;padding:16px 0 0}
.offer-box p{font-size:14px;font-weight:600;line-height:20px;padding:0 10px}
.offer-box hr{border:0;border-top:1px solid rgba(255,255,255,.4);width:226px;margin:0 auto}
.start{position:absolute;top:474px;left:567px;width:470px}
.start h3{font-family:"Dosis",sans-serif;font-weight:600;font-size:18px;color:#222}
.start p{font-size:14px;line-height:22px;color:#777;margin-top:18px}
.start .btn{position:absolute;top:256px;left:0;height:50px;padding:0 38px}
</style>
</head>
<body>

<header class="site-header">
  <div class="brand"><span class="brand-dot"></span>BrightPath Promotions Group</div>
  <nav class="top-links"><span>Log In</span><span>Sign Up</span></nav>
  <div class="contact-line">
    <div class="phone-badge"><svg width="16" height="16" viewBox="0 0 24 24"><path fill="#fff" d="M6.6 10.8a15 15 0 0 0 6.6 6.6l2.2-2.2c.3-.3.7-.4 1-.2 1.1.4 2.3.6 3.6.6.6 0 1 .4 1 1V20c0 .6-.4 1-1 1A17 17 0 0 1 3 4c0-.6.4-1 1-1h3.5c.6 0 1 .4 1 1 0 1.3.2 2.5.6 3.6.1.3 0 .7-.2 1z"/></svg></div>
    <p>USA Office : 555-210-4836<br>International : 1-800-555-0147</p>
  </div>
  <div class="header-rule"></div>
  <nav class="main-nav"><span>Home</span><span>Our Incentives</span><span>Samples</span><span>Affiliates</span><span>Testimonials</span><span>Faqs</span><span class="active">Contact</span></nav>
</header>

<section class="hero" role="img" aria-label="Dark teal photo of a business handshake">
  <svg class="hero-shapes" width="1200" height="472"><polygon points="640,472 1200,395 1200,472" fill="var(--blue)"/></svg>
  <div class="hero-copy">
    <h1>PREMIUM INCENTIVE MARKETING SERVICES</h1>
    <p>Boost Sales From Your Existing Marketing Efforts Creating Exciting Promotions<br>With Access To Unlimited Quantity of Our Incentive Certificates</p>
  </div>
  <div class="hero-actions">
    <span class="btn">Sign Up For Free 30 day Trial</span>
    <span class="watch"><span><svg width="12" height="12" viewBox="0 0 12 12"><polygon points="3,1 11,6 3,11" fill="#fff"/></svg></span>Watch Video</span>
  </div>
</section>
<svg style="position:absolute;top:574px;left:0" width="1200" height="90"><polygon points="0,0 1150,0 0,89" fill="var(--orange)"/></svg>

<section class="right-fit">
  <h2 class="heading">Right Fit And Logical Choice</h2>
  <p class="sub">See How We Are Better Than others</p>
  <div class="stats">
    <div class="stat"><svg width="70" height="70" viewBox="0 0 70 70" fill="none" stroke="var(--blue)" stroke-width="2.5"><rect x="24" y="4" width="40" height="60"/><path d="M32 16h24M32 26h24M32 36h24" stroke="var(--orange)"/><circle cx="18" cy="38" r="8"/><path d="M4 66c0-10 6-16 14-16s14 6 14 16z"/></svg>14+ Years In<br>Business</div>
    <div class="stat"><svg width="76" height="70" viewBox="0 0 76 70"><g fill="var(--orange)"><circle cx="20" cy="12" r="7"/><circle cx="38" cy="12" r="7"/><circle cx="56" cy="12" r="7"/></g><g fill="var(--blue)"><circle cx="14" cy="36" r="8"/><circle cx="38" cy="34" r="9"/><circle cx="62" cy="36" r="8"/><path d="M0 62c0-12 6-16 14-16s14 4 14 16zM22 66c0-14 7-20 16-20s16 6 16 20zM48 62c0-12 6-16 14-16s14 4 14 16z"/></g></svg>15,000+ Clients<br>Enrolled</div>
    <div class="stat"><svg width="60" height="70" viewBox="0 0 60 70" fill="none" stroke="var(--blue)" stroke-width="2.5"><rect x="6" y="3" width="48" height="62"/><path d="M16 16h28M16 25h28" stroke="var(--orange)"/><circle cx="30" cy="44" r="7"/><path d="M25 50l-3 12 8-4 8 4-3-12"/></svg>4+ Million Certificates<br>Distributed</div>
    <div class="stat"><svg width="70" height="70" viewBox="0 0 70 70" fill="none" stroke="var(--blue)" stroke-width="2.5"><rect x="4" y="22" width="62" height="14"/><rect x="9" y="36" width="52" height="30"/><path d="M30 22v44M40 22v44" stroke="var(--orange)"/><path d="M35 22c-8-14-22-10-14 0M35 22c8-14 22-10 14 0" stroke="var(--orange)"/></svg>Hundreds Of Thousands<br>Of Redemptions</div>
    <div class="stat"><svg width="70" height="70" viewBox="0 0 70 70" fill="none" stroke-width="2.5"><circle cx="36" cy="20" r="9" stroke="var(--orange)"/><circle cx="36" cy="20" r="15" stroke="var(--orange)" stroke-dasharray="5 4"/><path d="M4 50c10-6 18-6 26 0h18c4 0 4 6 0 6H30M4 62c12 4 30 4 44-4l18-12" stroke="var(--blue)"/></svg>Top Notch Customer<br>Service</div>
    <div class="stat"><svg width="70" height="70" viewBox="0 0 70 70" fill="none" stroke="var(--blue)" stroke-width="2.5"><rect x="4" y="4" width="62" height="46"/><path d="M14 16h42M14 24h42M14 32h28" stroke="var(--orange)"/><circle cx="35" cy="46" r="8"/><path d="M30 52l-3 14 8-4 8 4-3-14"/></svg>Licensed Seller Of<br>Travel CST #4075318</div>
  </div>
</section>

<section class="certs">
  <h2 class="heading">Unlimited Amount of Gift certificates</h2>
  <p class="sub">For $99/Mo You CanAttract More Customers By Creating Sxciting Promotional Giveaways Using an unimited amount of certificates redeemable for :</p>
  <div class="cert-grid">
    <div class="cert">
      <div class="cert-photo" role="img" aria-label="Airplane flying through clouds" style="background:linear-gradient(#6d8a9c,#c9d6de)"></div>
      <div class="cert-label">Vacation Getaway Certificates</div>
      <p class="cert-text">Resort Stays, Cruises &amp; Airfares<br>Up To <b>$3000.00</b> Retail Value Your<br>Customers Just Pay Taxes!</p>
      <div class="cert-link">View Certifications <svg width="24" height="10"><path d="M0 5h22M17 1l5 4-5 4" stroke="var(--blue)" fill="none" stroke-width="1.5"/></svg></div>
    </div>
    <div class="cert">
      <div class="cert-photo" role="img" aria-label="Restaurant table with plates of fries" style="background:linear-gradient(135deg,#2a2420,#6b4a2a 50%,#2e2622)"></div>
      <div class="cert-label">Restaurant Gift Certificates</div>
      <p class="cert-text"><b>$25-$300</b> Retail Value<br>Thousands Of Restaurants<br>Nationwide!</p>
      <div class="cert-link">View Certifications <svg width="24" height="10"><path d="M0 5h22M17 1l5 4-5 4" stroke="var(--blue)" fill="none" stroke-width="1.5"/></svg></div>
    </div>
    <div class="cert">
      <div class="cert-photo" role="img" aria-label="Desk with laptops, tablets and gadgets" style="background:linear-gradient(135deg,#8c8f8e,#c5c4be 50%,#7b7f80)"></div>
      <div class="cert-label">Electronic Product Giveaways</div>
      <p class="cert-text">HD Tablets, Premium Earbuds,<br>Smart Watches, Mp4 Players<br><b>$100-$199</b> Retail Value</p>
      <div class="cert-link">View Certifications <svg width="24" height="10"><path d="M0 5h22M17 1l5 4-5 4" stroke="var(--blue)" fill="none" stroke-width="1.5"/></svg></div>
    </div>
    <div class="cert">
      <div class="cert-photo" role="img" aria-label="Red neon wine sign" style="background:linear-gradient(90deg,#3a0508,#b3121c 50%,#3a0508)"></div>
      <div class="cert-label">Gas, Grocery &amp; Wine Vouchers</div>
      <p class="cert-text">Available In <b>$50-$100</b><br>Denomination</p>
      <div class="cert-link">View Certifications <svg width="24" height="10"><path d="M0 5h22M17 1l5 4-5 4" stroke="var(--blue)" fill="none" stroke-width="1.5"/></svg></div>
    </div>
  </div>
  <span class="btn">Get A 100% Free Sample Package</span>
</section>

<section class="areas">
  <h2 class="heading">We Plug Right Into Your Existing advertising In 4 Major areas</h2>
  <article class="area" style="top:175px;left:252px">
    <div class="area-photo" role="img" aria-label="Chess pieces on a board" style="background:linear-gradient(135deg,#1d2a3a,#6f7f90)"></div>
    <div class="area-body"><h3>Boost Response Rates To<br>Your Existing Ads</h3><p>Add a simple tagline to all your ads "Contact us today and receive Two Nights In Las Vegas, No Purchase Necessary!</p></div>
  </article>
  <article class="area" style="top:175px;left:613px">
    <div class="area-photo" role="img" aria-label="Business handshake" style="background:linear-gradient(135deg,#2b2b2b,#8a7d6e)"></div>
    <div class="area-body"><h3>Get More New Customers</h3><p>Now that you have generated a new lead go ahead and offer a higher valued incentive like our Airfare Plus Hotel Getaway persuade them to purchase today vs tomorrow!</p></div>
  </article>
  <article class="area" style="top:347px;left:252px">
    <div class="area-photo" role="img" aria-label="Rising bar chart graphic" style="background:linear-gradient(135deg,#0e1a26,#1f6a8c)"></div>
    <div class="area-body"><h3>Increase Repeat &amp;<br>Referral Business</h3><p>You have a reason to contact your clients to remind them about your services with a 7 Night Resort Getway to motivate them to buy again!</p></div>
  </article>
  <article class="area" style="top:347px;left:613px">
    <div class="area-photo" role="img" aria-label="Hand pointing at charts on a tablet" style="background:linear-gradient(135deg,#e8eef4,#8fb4d6)"></div>
    <div class="area-body"><h3>Boost Your Referral Business</h3><p>Offer a $100 Wine Voucher or even our Two Night Bahama Cruise to entice your customers to send you a referral and then watch your referral business soar!</p></div>
  </article>
  <span class="btn">Quick 30 day Free trial Sign Up</span>
</section>

<section class="distribution">
  <h2 class="heading">Easy Distribution of incentive</h2>
  <svg class="connector" style="left:265px" width="110" height="70"><path d="M2 4l96 60M90 64h10v-10" stroke="var(--orange)" stroke-width="1.5" fill="none" stroke-dasharray="3 3"/></svg>
  <svg class="connector" style="left:530px;top:126px" width="110" height="70"><path d="M2 66l96-60M88 6h10v10" stroke="var(--orange)" stroke-width="1.5" fill="none" stroke-dasharray="3 3"/></svg>
  <svg class="connector" style="left:812px" width="110" height="70"><path d="M2 4l96 60M90 64h10v-10" stroke="var(--orange)" stroke-width="1.5" fill="none" stroke-dasharray="3 3"/></svg>
  <div class="channel" style="left:60px">
    <div class="ring"><svg width="50" height="50" viewBox="0 0 50 50" fill="none" stroke="var(--orange)" stroke-width="2.5"><rect x="14" y="4" width="22" height="12"/><rect x="4" y="16" width="42" height="20" rx="3"/><rect x="12" y="28" width="26" height="18"/><path d="M17 35h16M17 40h16"/></svg></div>
    <h3>Print</h3><p>Download PDF certificates to print and physically hand them out or mail them to your customers.</p>
  </div>
  <div class="channel" style="left:322px">
    <div class="ring"><svg width="50" height="50" viewBox="0 0 50 50" fill="none" stroke="var(--orange)" stroke-width="2.5"><rect x="4" y="10" width="38" height="28"/><path d="M4 10l19 16 19-16"/><path d="M34 40h12M42 36l4 4-4 4"/></svg></div>
    <h3>Email</h3><p>Email E-Certificates to your customers individually and in bulk with just one click.</p>
  </div>
  <div class="channel" style="left:601px">
    <div class="ring"><svg width="54" height="50" viewBox="0 0 54 50" fill="none" stroke="var(--orange)" stroke-width="2.5"><rect x="3" y="14" width="40" height="16" rx="3"/><text x="8" y="26" font-size="8" fill="var(--orange)" stroke="none" font-family="Raleway,sans-serif">http://</text><path d="M34 24l0 20 5-5 4 8 3-2-4-8h7z" fill="#fff"/></svg></div>
    <h3>Web Banners or API Integration</h3><p>Install our HTML web banners on the thank you pages of your website to automate distribution of our incentives and if you are tech savvy you can integrate our NEW API too!</p>
  </div>
  <div class="channel" style="left:879px">
    <div class="ring"><svg width="50" height="50" viewBox="0 0 50 50" fill="none" stroke="var(--orange)" stroke-width="2.5"><path d="M6 6h38v28H20l-10 9v-9H6z"/><circle cx="16" cy="20" r="2"/><circle cx="25" cy="20" r="2"/><circle cx="34" cy="20" r="2"/></svg></div>
    <h3>SMS/Text Messaging</h3><p>Send certificates through text messaging with just one click with our new SMS feature with no per sms fees!</p>
  </div>
  <div class="call-btn">Click And we will <em>Call You</em></div>
</section>

<section class="materials">
  <h2 class="heading">Promotional Marketing Materials To Help You<br>Promote The Incentive To Your Customers</h2>
  <div class="mat-grid">
    <div class="mat"><div class="mat-photo" role="img" aria-label="Flyer showing city lights at night" style="background:linear-gradient(135deg,#2a1a3a,#b3412a 50%,#2b2540)"></div><div class="mat-label">Posters &amp; Flyers</div></div>
    <div class="mat"><div class="mat-photo" role="img" aria-label="Video player on a screen" style="background:linear-gradient(135deg,#f2f2f2,#c9202a 55%,#eeeeee)"></div><div class="mat-label">Web Videos</div></div>
    <div class="mat"><div class="mat-photo" role="img" aria-label="Product description brochure page" style="background:linear-gradient(#1d3f7a 0 22%,#f4f4f4 22%)"></div><div class="mat-label">Product Description Brochures</div></div>
    <div class="mat"><div class="mat-photo" role="img" aria-label="Marketing tips document page" style="background:linear-gradient(#1d3f7a 0 22%,#fafafa 22%)"></div><div class="mat-label">Tips</div></div>
  </div>
  <aside class="offer-box">
    <h3>Get Promotional Design Material</h3>
    <p style="margin:45px 0 30px">You will get Professionally designed Flayers &amp; Posters</p>
    <hr>
    <p style="margin:30px 0 28px">You will also Get Professioanl Marketing Tips</p>
    <hr>
    <p style="margin-top:28px">and Much More...</p>
  </aside>
  <div class="start">
    <h3>Start Today</h3>
    <p>We help you by providing full color, professionally designed flyers &amp; posters for each incentive that you can get printed at your local print shop or any online printing company.</p>
    <p>We also provide you with customer appreciation letter templates and warm lead letter templates as well as proven incentive marketing tips and strategies to help you get the most from promotional campaigns.</p>
    <span class="btn">Contact Us Direct Today</span>
  </div>
</section>

</body>
</html>
```